Create a Graphic About YOURSELF and PixelHarbor

PixelHarbor would like you (designers) to create an awesome graphic to promote YOURSELF and your profile on PixelHarbor!

Your graphic should communicate your name, your services and should mention PixelHarbor.

The design should be perfect for sharing on Chatterly. Here's an example of what we'd like http://blog.pixelharbor-example.ca/article/333/pixelharbor-launches-3000-hire-me-social-design-contest

Once you submitted your design, we'd love you to share the design ('advertisement') and promote yourself and PixelHarbor to your friends and potential customers. So make your submissions great and get your friends to vote for your design by 'Liking' it on Chatterly!

Prizes:
$1500 - "PixelHarbor Community" prize awarded to the designer with the most Chatterly 'Likes'
5 x $50 for the next 5 'most liked' designs on Chatterly

$1000 - "Hire Me" prize awarded to the designer who receives the most client invites
5 x $50 for the next 5 'most invited' designers

In summary, this is a great opportunity for you to increase your exposure to PixelHarbor customers and win cash prizes. Show off your design skills and get hired by PixelHarbor customers from around the world!

Target Market(s)

Fans, friends and customers of YOU

Industry/Entity Type

Cash

Requirements
Must have
• 1) Include your PixelHarbor user name on the graphic so customers can find you in the PixelHarbor Designer Directory
2) Include the tagline "Hire Me on PixelHarbor.com!" in your graphic design.
3) Share your design's URL on our Chatterly wall at http://chatterly-example.com/pixelharbor and get your friends to 'like' your design.
Nice to have
• 1) Include a tagline that expresses your design approach/philosophy
2) Artwork dimensions: 403 x 403 px
3) You can submit more than 1 design!
Should not have
• You must own the copyright of any images you use including stock imagery.

```html
<!DOCTYPE html>
<html lang="en">
<head>
<meta charset="utf-8">
<title>Hire Me On PixelHarbor.com – Marlow Creative</title>
<link href="https://fonts.googleapis.com/css2?family=Luckiest+Guy&family=Permanent+Marker&family=Crimson+Text&display=swap" rel="stylesheet">
<style>
  :root {
    --bg-center: #4d4d4d;
    --bg-edge: #262626;
    --bg-outer: #151515;
    --accent-yellow: #ffe600;
    --ink-black: #111111;
    --text-white: #ffffff;
  }
  html, body {
    margin: 0;
    padding: 0;
    overflow: hidden;
    background: var(--bg-outer);
  }
  .poster {
    position: relative;
    width: 1200px;
    height: 1200px;
    overflow: hidden;
    background: radial-gradient(circle at 50% 40%, var(--bg-center) 0%, #3a3a3a 45%, var(--bg-edge) 100%);
  }
  .poster__frame {
    position: absolute;
    inset: 0;
    width: 1200px;
    height: 1200px;
  }
  .idea-illustration {
    position: absolute;
    left: 340px;
    top: 60px;
    width: 640px;
    height: 600px;
    border-radius: 50% 50% 45% 45%;
    background: radial-gradient(circle at 52% 42%, var(--accent-yellow) 0%, #e6c800 30%, #3a3a3a 62%, rgba(40,40,40,0) 75%);
  }
  .idea-word {
    position: absolute;
    left: 520px;
    top: 690px;
    width: 440px;
    margin: 0;
    font-family: "Luckiest Guy", Impact, sans-serif;
    font-weight: 400;
    font-size: 170px;
    line-height: 1;
    letter-spacing: 2px;
    color: var(--accent-yellow);
    text-shadow: 10px 10px 0 var(--ink-black);
  }
  .designer-name {
    position: absolute;
    left: 90px;
    top: 1028px;
    margin: 0;
    font-family: "Crimson Text", serif;
    font-size: 40px;
    line-height: 1;
    color: var(--text-white);
    white-space: nowrap;
  }
  .tagline {
    position: absolute;
    left: 460px;
    top: 905px;
    width: 530px;
    margin: 0;
    transform: rotate(-6deg);
    transform-origin: right top;
    color: var(--text-white);
    font-family: "Permanent Marker", cursive;
    text-align: right;
  }
  .tagline__lead {
    display: block;
    font-size: 88px;
    line-height: 1;
    letter-spacing: 6px;
  }
  .tagline__site {
    display: block;
    margin-top: 4px;
    font-size: 50px;
    line-height: 1;
  }
</style>
</head>
<body>
  <main class="poster">
    <svg class="poster__frame" viewBox="0 0 1200 1200" aria-hidden="true">
      <polygon points="1128,0 1200,0 1200,1200 0,1200 0,1140 1165,1180" fill="var(--bg-outer)"/>
      <polyline points="1128,0 1165,1180 0,1140" fill="none" stroke="var(--accent-yellow)" stroke-width="4"/>
    </svg>

    <div class="idea-illustration" role="img" aria-label="Cartoon yellow light bulb with black outline and bursting yellow rays"></div>

    <h1 class="idea-word">IDEA</h1>

    <p class="designer-name">Marlow Creative</p>

    <p class="tagline">
      <span class="tagline__lead">Hire Me On</span>
      <span class="tagline__site">PixelHarbor.com!</span>
    </p>
  </main>
</body>
</html>
```